Lumora business card for a plastic surgeon

we need a business card for plastic surgeons that work on a clinic called LUMORA.
we want a clean design and the following informations: name of the doctor, doctor's registration number (called CRM), telephone, address, facebook, instagram.
Colors: white, blue tones, light brown/ coffee

facebook and instagram: lumoraesteticaclinica

Industry/Entity Type

Business

Contact Information for Business Card

clean design

Font styles to use
Serif
Sans Serif
Other font styles liked:
• helvetica light

Colors
cee9f5
85cae6
85abd2
3276b5
cfeae6
cedeed
eaf1f7

Requirements
Must have
• doctor's name
• identification number (called CRM)
• contact (phone, facebook, instagram, address)

```html
<!DOCTYPE html>
<html lang="pt">
<head>
<meta charset="utf-8">
<title>Lumora – Business Card</title>
<link rel="stylesheet" href="https://fonts.googleapis.com/css2?family=Cinzel:wght@400&family=Lora:wght@700&family=Roboto:wght@400&display=swap">
<style>
  :root {
    --canvas: #e6e6e8;
    --card: #f8fafc;
    --card-front: #eef4fa;
    --sky: #6bbdd6;
    --navy: #1f3d6b;
    --coffee: #a8917a;
    --shadow: rgba(40, 40, 48, 0.28);
  }
  * { box-sizing: border-box; margin: 0; padding: 0; }
  html, body { width: 1200px; height: 1200px; overflow: hidden; }
  body { background: var(--canvas); position: relative; font-family: "Roboto", Arial, sans-serif; }

  .card {
    position: absolute;
    width: 712px;
    height: 418px;
    box-shadow: 0 18px 30px var(--shadow);
  }
  .card--front { left: 238px; top: 119px; background: var(--card-front); }
  .card--back  { left: 230px; top: 645px; height: 417px; background: var(--card); }

  .brand { position: absolute; text-align: center; }
  .brand__name {
    font-family: "Cinzel", Georgia, serif;
    font-weight: 400;
    color: var(--sky);
    line-height: 1;
    letter-spacing: 2px;
  }
  .brand__tagline {
    font-family: "Cinzel", Georgia, serif;
    font-weight: 400;
    color: var(--navy);
    line-height: 1;
    letter-spacing: 1px;
  }

  .card--front .brand { left: 0; right: 0; top: 146px; }
  .card--front .brand__name { font-size: 84px; }
  .card--front .brand__tagline { font-size: 32px; margin-top: 30px; }

  .card--back .brand { left: 40px; width: 320px; top: 160px; }
  .card--back .brand__name { font-size: 66px; }
  .card--back .brand__tagline { font-size: 26px; margin-top: 22px; }

  .details { position: absolute; left: 386px; top: 62px; color: var(--navy); }
  .details__name { font-family: "Lora", Georgia, serif; font-weight: 700; font-size: 27px; line-height: 1.3; }
  .details__crm { font-size: 16px; margin-top: 6px; }

  .list { list-style: none; font-size: 18px; line-height: 25px; }
  .list li { display: flex; align-items: center; gap: 10px; }
  .list--social { margin-top: 26px; }
  .list--contact { margin-top: 26px; }
  .list--contact li { gap: 16px; }
  .social-mark { width: 18px; height: 18px; border-radius: 4px; background: var(--coffee); flex: none; }
  .icon { width: 18px; height: 18px; flex: none; }

  .address { font-size: 18px; line-height: 23px; margin-top: 14px; }
</style>
</head>
<body>

  <section class="card card--front">
    <div class="brand">
      <div class="brand__name">LUMORA</div>
      <div class="brand__tagline">CIRURGIA PLÁSTICA</div>
    </div>
  </section>

  <section class="card card--back">
    <div class="brand">
      <div class="brand__name">LUMORA</div>
      <div class="brand__tagline">CIRURGIA PLÁSTICA</div>
    </div>

    <div class="details">
      <h1 class="details__name">Dr. Rafael Moreira</h1>
      <p class="details__crm">CRM: 123456789</p>

      <ul class="list list--social">
        <li><span class="social-mark" aria-label="Facebook"></span>lumoraesteticaclinica</li>
        <li><span class="social-mark" aria-label="Instagram"></span>lumoraesteticaclinica</li>
      </ul>

      <ul class="list list--contact">
        <li>
          <svg class="icon" viewBox="0 0 18 18" aria-label="Telefone"><path d="M2 6c0-2 3-3 7-3s7 1 7 3v1h-3V6H5v1H2z M5 8h8l2 6H3z" fill="var(--coffee)"/></svg>
          +00 555 010 2020
        </li>
        <li>
          <svg class="icon" viewBox="0 0 18 18" aria-label="Site"><g fill="none" stroke="var(--coffee)" stroke-width="1.4"><circle cx="9" cy="9" r="6.5"/><ellipse cx="9" cy="9" rx="3" ry="6.5"/><path d="M2.5 9h13"/></g></svg>
          www.lumoraclinica.com
        </li>
        <li>
          <svg class="icon" viewBox="0 0 18 18" aria-label="E-mail"><rect x="2" y="4" width="14" height="10" fill="var(--coffee)"/><path d="M2 4l7 6 7-6" fill="none" stroke="#fff" stroke-width="1.2"/></svg>
          contato@lumoraclinica.com
        </li>
      </ul>

      <p class="address">Your Long Commercial or<br>business address in 2 line</p>
    </div>
  </section>

</body>
</html>
```